Fitness competition business needs a card design

I need a professional business card design using my logo. The card will be horizontal with rounded edges.

Target Market(s)

Female fitness competitors

Industry/Entity Type

Fitness

Contact Information for Business Card

Rose-Lynn Darby
Owner
stagevarno.com
555.301.2187
info@stagevarno.com

Font styles to use
Serif

Colors

Designer to choose colors to be used in the design.

Requirements
Must have
• On the back please add the following:
• Figure
• Bikini
• Physique
• Fitness
Nice to have
• Looking for a very sleek design, contemporary and easy to read.
Should not have
• Should not be difficult to read or be too busy

```html
<!DOCTYPE html>
<html lang="en">
<head>
<meta charset="utf-8">
<title>Stage Varno – Business Card</title>
<link rel="stylesheet" href="https://fonts.googleapis.com/css2?family=Oswald:wght@500;600&family=Tinos&display=swap">
<style>
  :root {
    --canvas: #ece9e4;
    --red: #e8202a;
    --grey-dark: #4b4b4e;
    --grey-mid: #5d5d60;
    --grey-text: #505053;
    --white: #ffffff;
    --paper-top: #f6f6f6;
    --paper-bottom: #e9e9ea;
  }
  * { box-sizing: border-box; margin: 0; padding: 0; }
  html, body {
    width: 1200px; height: 545px; overflow: hidden;
    background: var(--canvas);
  }
  .canvas { position: relative; width: 1200px; height: 545px; }

  .card {
    position: absolute; top: 117px;
    height: 301px; border-radius: 22px; overflow: hidden;
    box-shadow: 0 6px 14px rgba(0,0,0,0.25);
  }

  /* Front */
  .card-front {
    left: 67px; width: 518px;
    background: linear-gradient(90deg, var(--grey-mid) 0%, #8a4a4d 45%, var(--red) 100%);
    color: var(--white);
    text-align: center;
  }
  .front-brand {
    position: absolute; left: 0; right: 0; top: 168px;
    font-family: "Oswald", sans-serif; font-weight: 600;
    font-size: 34px; letter-spacing: 1px; line-height: 1;
  }
  .front-disciplines {
    position: absolute; left: 0; right: 0; top: 258px;
    font-family: "Tinos", serif; font-size: 13.5px; letter-spacing: 0.6px;
  }
  .front-disciplines .dot { margin: 0 7px; }

  /* Back */
  .card-back {
    left: 621px; width: 514px;
    background: linear-gradient(180deg, var(--paper-top) 0%, var(--white) 45%, var(--paper-bottom) 100%);
  }
  .holder-name {
    position: absolute; left: 39px; top: 45px;
    font-family: "Oswald", sans-serif; font-weight: 500;
    font-size: 19px; color: var(--grey-text); line-height: 1;
  }
  .holder-role {
    position: absolute; left: 39px; top: 68px;
    font-family: "Oswald", sans-serif; font-weight: 500;
    font-size: 13px; color: var(--red); line-height: 1;
  }
  .back-brand {
    position: absolute; right: 32px; top: 110px;
    font-family: "Oswald", sans-serif; font-weight: 600;
    font-size: 27px; color: var(--red); line-height: 1; letter-spacing: 0.5px;
  }
  .contact-list {
    position: absolute; left: 40px; top: 210px; list-style: none;
    font-family: "Tinos", serif; font-size: 13.5px; color: var(--grey-text);
  }
  .contact-list li { display: flex; align-items: center; height: 20px; }
  .contact-list svg { margin-right: 8px; }
  .footer-bands { position: absolute; left: 0; bottom: 0; }
  .website {
    position: absolute; left: 307px; bottom: 8px;
    display: flex; align-items: center;
    font-family: "Tinos", serif; font-size: 13.5px; color: var(--white);
  }
  .website svg { margin-right: 6px; }
</style>
</head>
<body>
<div class="canvas">

  <section class="card card-front" aria-label="Card front">
    <div class="front-brand">STAGE VARNO</div>
    <p class="front-disciplines">FIGURE<span class="dot">•</span>BIKINI<span class="dot">•</span>PHYSIQUE<span class="dot">•</span>FITNESS</p>
  </section>

  <section class="card card-back" aria-label="Card back">
    <h1 class="holder-name">ROSE-LYNN DARBY</h1>
    <p class="holder-role">OWNER</p>
    <div class="back-brand">STAGE VARNO</div>

    <ul class="contact-list">
      <li>
        <svg width="16" height="16" viewBox="0 0 16 16" aria-hidden="true">
          <circle cx="8" cy="8" r="8" fill="var(--red)"/>
          <path d="M5.2 4.2l1.5-.4 1 2-1 .8a5 5 0 0 0 2.2 2.2l.8-1 2 1-.4 1.5c-3 .3-6.4-3.1-6.1-6.1z" fill="#fff"/>
        </svg>555.301.2187
      </li>
      <li>
        <svg width="16" height="16" viewBox="0 0 16 16" aria-hidden="true">
          <circle cx="8" cy="8" r="8" fill="var(--red)"/>
          <rect x="4" y="5" width="8" height="6" fill="#fff"/>
          <path d="M4 5l4 3.2L12 5" fill="none" stroke="var(--red)" stroke-width="1"/>
        </svg>info@stagevarno.com
      </li>
    </ul>

    <svg class="footer-bands" width="514" height="32" viewBox="0 0 514 32" aria-hidden="true">
      <polygon points="0,13 252,13 240,32 0,32" fill="var(--red)"/>
      <polygon points="264,0 514,0 514,32 242,32" fill="var(--grey-dark)"/>
    </svg>
    <div class="website">
      <svg width="14" height="14" viewBox="0 0 14 14" aria-hidden="true">
        <circle cx="7" cy="7" r="7" fill="var(--red)"/>
        <circle cx="7" cy="7" r="4" fill="none" stroke="#fff" stroke-width="0.9"/>
        <ellipse cx="7" cy="7" rx="1.7" ry="4" fill="none" stroke="#fff" stroke-width="0.9"/>
        <line x1="3" y1="7" x2="11" y2="7" stroke="#fff" stroke-width="0.9"/>
      </svg>stagevarno.com
    </div>
  </section>

</div>
</body>
</html>
```